Label for moisturizing face lotion - skin care

I need a label for a face moisturizer. Please see the details in the attachments. I also attached two variations of the logo.
The fonts are Futura PT for body
Orpheus Pro for header

We are looking for something very modern, simple, just black and white. It's an all natural product.
Please add under the logo:
with Phytoplankton extract and hyaluronic acid

Target Market(s)

Women

Industry/Entity Type

Skin care

Font styles to use
Sans Serif
Other font styles liked:
• Futura PT for body Orpheus Pro for header

Colors

Designer to choose only greyscale colors for use in the design.

Requirements
Nice to have
• White label with black letters, simple, clean, no serifs

```html
<!DOCTYPE html>
<html lang="en">
<head>
<meta charset="utf-8">
<title>Vela Anti-Aging Moisturizer – Label</title>
<link href="https://fonts.googleapis.com/css2?family=Jost:wght@400;500;700&family=Cormorant+Garamond:wght@400;500&display=swap" rel="stylesheet">
<style>
  :root {
    --ink: #141414;
    --ink-soft: #3a3a3a;
    --paper: #ffffff;
    --backdrop: #ececec;
    --edge: #d2d2d2;
  }
  * { box-sizing: border-box; margin: 0; padding: 0; }
  html, body {
    width: 1200px; height: 600px; overflow: hidden;
    background: var(--backdrop);
  }
  body {
    display: flex; align-items: center; justify-content: center;
    font-family: "Jost", "Futura", sans-serif; color: var(--ink);
  }
  .label {
    width: 1140px; height: 320px;
    background: var(--paper);
    border: 1px solid var(--edge);
    display: grid; grid-template-columns: repeat(3, 1fr);
  }
  .panel { padding: 40px 34px; position: relative; }
  .panel + .panel { border-left: 1px dashed var(--edge); }

  /* Ingredients */
  .ingredients {
    font-size: 12.2px; line-height: 1.52; text-align: justify;
    color: var(--ink-soft); padding-top: 64px;
  }
  .ingredients strong { color: var(--ink); font-weight: 700; letter-spacing: 0.02em; }

  /* Front */
  .front { display: flex; flex-direction: column; align-items: center; padding-top: 34px; }
  .brand-mark {
    width: 54px; height: 54px; border: 1px solid var(--ink); border-radius: 50%;
    display: flex; align-items: center; justify-content: center;
    font-size: 19px; font-weight: 400; letter-spacing: 0.04em;
  }
  .brand-by { margin-top: 8px; font-size: 6.5px; letter-spacing: 0.4em; }
  .product-name {
    margin-top: 14px;
    font-family: "Cormorant Garamond", "Didot", serif; font-weight: 400;
    font-size: 74px; line-height: 0.9; letter-spacing: 0.14em; padding-left: 0.14em;
  }
  .product-type { margin-top: 8px; font-size: 12.5px; letter-spacing: 0.24em; }
  .product-claim {
    margin-top: 20px; font-size: 7px; letter-spacing: 0.32em;
    text-align: center; line-height: 1.5;
  }

  /* Back */
  .back { display: grid; grid-template-columns: 1.15fr 1fr; gap: 16px; padding-top: 60px; }
  .section-title { font-size: 12px; font-weight: 700; letter-spacing: 0.02em; }
  .section-note { font-size: 4px; margin-top: 1px; color: var(--ink-soft); }
  .benefit-list { list-style: none; margin-top: 12px; }
  .benefit-list li { font-size: 11px; line-height: 1; margin-bottom: 13px; padding-left: 12px; position: relative; }
  .benefit-list li::before { content: "•"; position: absolute; left: 0; }
  .maker-lines { margin-top: 14px; font-size: 10px; letter-spacing: 0.28em; line-height: 2.15; color: var(--ink-soft); }
</style>
</head>
<body>
  <main class="label">
    <section class="panel ingredients">
      <p><strong>INGREDIENTS:</strong> deionized water, cocos nucifera oil, stearic acid, emulsifying wax, hyaluronic acid, citric acid, glycerin, populous tremuloides bark extract, plankton extract (nannochloropsis gaditana, isochrysis galbana, phaeodactylum tricornutum, tetraselmis chuii, dunaliella salina), plankton powder (nannochloropsis gaditana, isochrysis galbana, phaeodactylum tricornutum, tetraselmis chuii, dunaliella salina), lonicera caprifolium (honeysuckle absolute oil).</p>
    </section>

    <section class="panel front">
      <div class="brand-mark">HL</div>
      <p class="brand-by">BY. DR HOLT</p>
      <h1 class="product-name">VELA</h1>
      <p class="product-type">ANTI-AGING MOISTURIZER</p>
      <p class="product-claim">WITH PHYTOPLANKTON EXTRACT<br>AND HYALURONIC ACID</p>
    </section>

    <section class="panel back">
      <div class="benefits">
        <h2 class="section-title">BENEFITS</h2>
        <p class="section-note">• Strengthens skin hydration</p>
        <ul class="benefit-list">
          <li>Increases skin elasticity</li>
          <li>Stimulates skin cell growth</li>
          <li>Anti-wrinkle effect</li>
          <li>Antioxidant enhancer</li>
          <li>Improvement of ageing spots.</li>
        </ul>
      </div>
      <div class="maker">
        <h2 class="section-title">MANUFACTURER</h2>
        <p class="maker-lines">Marlow Lab<br>For: The Linden Co.<br>42 Harbor Road<br>27 Oakfield Drive</p>
      </div>
    </section>
  </main>
</body>
</html>
```